Luxury Coffee & Tea Package Design

I need a logo design and package design for a luxury coffee and tea brand on degassing valve bag for the coffee (biodegradable) and a biodegradable paper tube. I source hand selected tea and coffee blends from growers around the world and will need our brand to reflect the value of the product. See description below

Name of brand: Velorin Gourmet Coffees & Teas
Coffee Bag: Royal Blue Degassed Valve bag with gold sides
Tea Cylinder Tube: Dark Green biodegradable paper tube with gold lid.

Hex Code for the colors:
Royal Blue: #4169e1 for coffee bag
Green : #043927 for tea container
Gold: for both coffee and tea. use this link to get this balance of luxury gold: https://www.pinboardly.example/pin/381926475502817364/
https://www.pinboardly.example/pin/381926475502817364/

Let me know if you have questions. The attached images are examples we love.

Target Market(s)

men and women ages 30-55, coffee and tea lovers

Industry/Entity Type

food and beverage

Font styles to use
Sans Serif
Decorative

Colors
0054AA
0677BA
7BADD7
CADEEF
E8F1F8
00AB8E
00BBA5
67D7C9
C6EFE9
E9F9F6
FFC000
F8CF3A
FAE287
FDF2CF
FEFAEE

Requirements
Must have
• a luxury look, a modern logo that is attractive and easily identifiable with the product.
Nice to have
• some kind of pattern on the side of the gusseted bag
Should not have
• copycat logos from competitors or too plain of a logo

```html
<!DOCTYPE html>
<html lang="en">
<head>
<meta charset="utf-8">
<title>Velorin Gourmet Coffees &amp; Teas – Coffee Bag</title>
<link href="https://fonts.googleapis.com/css2?family=Josefin+Sans:wght@400;600;700&display=swap" rel="stylesheet">
<style>
:root{
  --bg:#e6e6e6;
  --ink:#1f1b1c;
  --royal:#4169e1;
  --royal-faint:#5a80ec;
  --label-black:#0b0b0b;
  --label-navy:#213a78;
  --gold-dark:#b07a2a;
  --gold-mid:#e7c25a;
  --gold-light:#f8e487;
  --white:#ffffff;
  --gold-grad:linear-gradient(90deg,var(--gold-dark),var(--gold-light) 50%,var(--gold-mid) 80%,var(--gold-dark));
}
*{box-sizing:border-box;margin:0;padding:0}
html,body{width:1044px;height:1200px;overflow:hidden}
body{background:var(--bg);font-family:"Josefin Sans",sans-serif;color:var(--ink);position:relative}

.brand-lockup{position:absolute;top:95px;left:0;width:1044px;display:flex;justify-content:center;align-items:center;gap:22px}
.brand-mark{width:110px;height:110px;border:4px solid var(--ink);border-radius:50%}
.brand-name{font-weight:700;font-size:44px;line-height:1.15;letter-spacing:3px;color:var(--ink)}
.brand-name span{display:block;font-size:22px;letter-spacing:1px}

.bag{position:absolute;top:395px;width:440px;height:745px;background:var(--royal);border-radius:4px;overflow:hidden}
.bag--black{left:62px}
.bag--navy{left:542px}
.bag-gusset{position:absolute;left:0;top:0;width:26px;height:100%;background:var(--gold-grad)}
.bag-seal-line{position:absolute;left:26px;right:0;top:34px;height:2px;background:rgba(255,255,255,.12)}
.bag-valve{position:absolute;top:68px;right:48px;width:54px;height:54px;border-radius:50%;background:rgba(255,255,255,.18)}
.bag-brand{position:absolute;top:130px;left:26px;right:0;text-align:center;color:var(--royal-faint);font-weight:700;font-size:34px;letter-spacing:4px;line-height:1.2}
.bag-brand span{display:block;font-size:17px;letter-spacing:1px}

.label{position:absolute;left:70px;top:268px;width:340px;height:425px;border-radius:20px;overflow:hidden;color:var(--white)}
.bag--black .label{background:var(--label-black)}
.bag--navy .label{background:var(--label-navy)}

.origin-band{position:absolute;left:38px;top:0;width:78px;height:345px;background:var(--gold-grad);border-radius:0 0 39px 39px}
.origin-name{position:absolute;left:77px;top:240px;transform:translate(-50%,-50%) rotate(-90deg);font-weight:700;font-size:26px;letter-spacing:2px;color:var(--label-black);white-space:nowrap}
.seal{position:absolute;left:29px;top:36px;width:96px;height:96px;border-radius:50%;background:var(--label-black);border:4px solid var(--gold-mid);display:flex;align-items:center;justify-content:center;text-align:center}
.seal-name{font-weight:700;font-size:13px;line-height:1.2;color:var(--gold-light)}
.seal-name span{display:block;font-size:7px}

.details{position:absolute;left:145px;top:130px;width:180px}
.eyebrow{font-size:6px;font-weight:700;letter-spacing:1px;line-height:1.3}
.flavour{margin-top:10px;font-size:11.5px;font-weight:700;letter-spacing:1.2px;line-height:1.35}
.badges{margin-top:12px;display:flex;align-items:center}
.badge{width:36px;height:36px;border-radius:50%;background:var(--gold-mid);border:2px solid var(--white);display:flex;flex-direction:column;align-items:center;justify-content:center;color:var(--label-black);font-size:4.6px;font-weight:700;text-align:center;line-height:1.1}
.badge svg{width:9px;height:9px;margin-bottom:1px}
.badge-link{flex:1;height:1px;background:var(--white);margin:0 2px}
.dots{margin-top:12px;border-top:2px dotted var(--gold-mid)}
.specs{display:flex;gap:8px;margin-top:8px;font-size:4.6px;line-height:1.6}
.specs div+div{border-left:1px dotted var(--white);padding-left:6px}
.roast{margin-top:3px;padding-left:34px;font-size:4.6px;display:flex;align-items:center;gap:3px}
.roast i{width:20px;height:5px;border-radius:3px;background:linear-gradient(90deg,var(--gold-mid) 55%,var(--white) 55%)}
.net{margin-top:12px;font-size:6px}
.distributor{margin-top:16px;font-size:6px;line-height:1.7}
.website{margin-top:42px;font-size:5.5px;font-weight:600;letter-spacing:1px}
.stamp{position:absolute;right:24px;bottom:40px;width:64px;height:64px;border-radius:50%;border:2px solid rgba(255,255,255,.25)}
</style>
</head>
<body>

<header class="brand-lockup">
  <div class="brand-mark"></div>
  <div class="brand-name">VELORIN<span>Gourmet Coffees &amp; Teas</span></div>
</header>

<section class="bag bag--black">
  <div class="bag-gusset"></div>
  <div class="bag-seal-line"></div>
  <div class="bag-valve"></div>
  <div class="bag-brand">VELORIN<span>Gourmet Coffees &amp; Teas</span></div>
  <div class="label">
    <div class="origin-band"></div>
    <div class="origin-name">COLOMBIA</div>
    <div class="seal"><div class="seal-name">VELORIN<span>Gourmet Coffees &amp; Teas</span></div></div>
    <div class="details">
      <p class="eyebrow">FLAVOUR<br>PROFILE</p>
      <p class="flavour">DRIED ORANGE,<br>BERRY, CHOCOLATE</p>
      <div class="badges">
        <div class="badge"><svg viewBox="0 0 10 10"><path d="M5 1a3 3 0 0 1 3 3c0 2-3 5-3 5S2 6 2 4a3 3 0 0 1 3-3z" fill="#0b0b0b"/></svg>SINGLE<br>ORIGIN</div>
        <div class="badge-link"></div>
        <div class="badge"><svg viewBox="0 0 10 10"><path d="M2 8C2 4 5 2 9 2c0 4-3 6-7 6z" fill="#0b0b0b"/></svg>FRESH</div>
        <div class="badge-link"></div>
        <div class="badge"><svg viewBox="0 0 10 10"><path d="M2 4h5v2a2.5 2.5 0 0 1-5 0zM7 5h1.5v1H7z" fill="#0b0b0b"/></svg>DELICIOUS</div>
      </div>
      <div class="dots"></div>
      <div class="specs">
        <div>ORIGIN: XXXX, COLOMBIA<br>ROAST DATE: 12-MAY-2023</div>
        <div>WHOLE BEAN / GROUND<br>GROUND: 0% - BEAN: 100%</div>
      </div>
      <div class="roast">ROAST LEVEL: MEDIUM <i></i></div>
      <div class="dots"></div>
      <p class="net">NET WT. XLB (XX OZ.) XXXG</p>
      <p class="distributor">DISTRIBUTED BY VELORIN ROASTER<br>LOCATION, AB 12345</p>
      <p class="website">WWW.VELORIN.EXAMPLE</p>
    </div>
    <div class="stamp"></div>
  </div>
</section>

<section class="bag bag--navy">
  <div class="bag-gusset"></div>
  <div class="bag-seal-line"></div>
  <div class="bag-valve"></div>
  <div class="bag-brand">VELORIN<span>Gourmet Coffees &amp; Teas</span></div>
  <div class="label">
    <div class="origin-band"></div>
    <div class="origin-name">COLOMBIA</div>
    <div class="seal"><div class="seal-name">VELORIN<span>Gourmet Coffees &amp; Teas</span></div></div>
    <div class="details">
      <p class="eyebrow">FLAVOUR<br>PROFILE</p>
      <p class="flavour">DRIED ORANGE,<br>BERRY, CHOCOLATE</p>
      <div class="badges">
        <div class="badge"><svg viewBox="0 0 10 10"><path d="M5 1a3 3 0 0 1 3 3c0 2-3 5-3 5S2 6 2 4a3 3 0 0 1 3-3z" fill="#0b0b0b"/></svg>SINGLE<br>ORIGIN</div>
        <div class="badge-link"></div>
        <div class="badge"><svg viewBox="0 0 10 10"><path d="M2 8C2 4 5 2 9 2c0 4-3 6-7 6z" fill="#0b0b0b"/></svg>FRESH</div>
        <div class="badge-link"></div>
        <div class="badge"><svg viewBox="0 0 10 10"><path d="M2 4h5v2a2.5 2.5 0 0 1-5 0zM7 5h1.5v1H7z" fill="#0b0b0b"/></svg>DELICIOUS</div>
      </div>
      <div class="dots"></div>
      <div class="specs">
        <div>ORIGIN: XXXX, COLOMBIA<br>ROAST DATE: 12-MAY-2023</div>
        <div>WHOLE BEAN / GROUND<br>GROUND: 0% - BEAN: 100%</div>
      </div>
      <div class="roast">ROAST LEVEL: MEDIUM <i></i></div>
      <div class="dots"></div>
      <p class="net">NET WT. XLB (XX OZ.) XXXG</p>
      <p class="distributor">DISTRIBUTED BY VELORIN ROASTER<br>LOCATION, AB 12345</p>
      <p class="website">WWW.VELORIN.EXAMPLE</p>
    </div>
    <div class="stamp"></div>
  </div>
</section>

</body>
</html>
```